Business Card for beauty technology startup

Design Glowra Business Card for a Beauty, based on the website identity and colors (https://www.glowra-example.com).
Glowra is a beauty tech startup that gathers helpful product info for beauty lovers and consumers (such as availability on stores, price range and product reviews) for makeup products. The card design must be young, colorful but clean, and very modern.

Target Market(s)

woman, 15-35

Industry/Entity Type

Cosmetics

Contact Information for Business Card

Full Name, address, phone

Font styles to use
Other font styles liked:
• Advent Pro

Colors
e34297
86cfc6
ffffff
5c5c5c
e8e8e8
e667a6
b2b2b2

Requirements
Must have
• One full colored side with a creative design and another with card info
• Use Color palette: #95C5C5 and/or #D38AA5
• Use fonts: Advent Pro
• Use website identity: https://www.glowra-example.com
Nice to have
• If needed extra font: Roboto

```html
<!DOCTYPE html>
<html lang="en">
<head>
<meta charset="utf-8">
<title>Glowra Business Card</title>
<link rel="stylesheet" href="https://fonts.googleapis.com/css2?family=Advent+Pro:wght@300;400&family=Open+Sans:wght@400;600&display=swap">
<style>
  :root {
    --bg: #262626;
    --card-dark: #2b2b2b;
    --card-light: #f1f1f1;
    --teal: #79c9c0;
    --teal-soft: #8fd3cb;
    --ink: #5c5c5c;
    --ink-dark: #444444;
  }
  * { margin: 0; padding: 0; box-sizing: border-box; }
  html, body { width: 1200px; height: 716px; overflow: hidden; background: var(--bg); }
  .stage { position: relative; width: 1200px; height: 716px; }
  .card {
    position: absolute; top: 210px; width: 520px; height: 297px;
    border-radius: 22px; box-shadow: 0 18px 40px rgba(0,0,0,.45);
  }
  .card--front { left: 45px; background: var(--card-dark); }
  .card--back { left: 635px; background: var(--card-light); }
  .brand { position: absolute; display: flex; align-items: center; gap: 18px; }
  .brand__dot {
    width: 48px; height: 48px; border-radius: 50%;
    border: 2px solid var(--teal);
  }
  .brand__name {
    font-family: "Advent Pro", sans-serif; font-weight: 300;
    color: var(--teal); font-size: 46px; letter-spacing: 10px; text-transform: uppercase;
  }
  .card--front .brand { left: 88px; top: 88px; }
  .website {
    position: absolute; left: 100px; top: 200px;
    font-family: "Open Sans", sans-serif; font-size: 14px; color: var(--teal-soft);
  }
  .card--back .brand { left: 34px; top: 58px; }
  .card--back .brand__name { font-size: 40px; letter-spacing: 8px; }
  .card--back .brand__dot { width: 42px; height: 42px; }
  .contact { position: absolute; left: 290px; top: 150px; font-family: "Open Sans", sans-serif; }
  .contact__name { font-size: 23px; color: var(--ink-dark); font-weight: 400; line-height: 1.05; }
  .contact__title { font-size: 13px; color: var(--teal); margin-bottom: 12px; }
  .contact__row { display: flex; gap: 7px; font-size: 12.5px; color: var(--ink); line-height: 1.35; margin-bottom: 6px; }
  .contact__row svg { flex: none; margin-top: 2px; }
  .social { position: absolute; left: 300px; bottom: 24px; display: flex; gap: 34px; }
  .social__item { width: 14px; height: 14px; border-radius: 3px; background: var(--teal); }
</style>
</head>
<body>
<main class="stage">
  <section class="card card--front">
    <div class="brand">
      <span class="brand__dot"></span>
      <span class="brand__name">Glowra</span>
    </div>
    <p class="website">www.glowra-example.com</p>
  </section>

  <section class="card card--back">
    <div class="brand">
      <span class="brand__dot"></span>
      <span class="brand__name">Glowra</span>
    </div>
    <div class="contact">
      <p class="contact__name">Your Name</p>
      <p class="contact__title">Job Title</p>
      <div class="contact__row">
        <svg width="12" height="12" viewBox="0 0 12 12" aria-hidden="true"><path d="M2.5 1h2l1 2.5-1.3 1a6 6 0 0 0 3.3 3.3l1-1.3L11 7.5v2c0 .8-.7 1.5-1.5 1.5A8.5 8.5 0 0 1 1 2.5C1 1.7 1.7 1 2.5 1z" fill="var(--teal)"/></svg>
        <span>000 000 0000</span>
      </div>
      <div class="contact__row">
        <svg width="12" height="14" viewBox="0 0 12 14" aria-hidden="true"><path d="M6 0a5 5 0 0 1 5 5c0 3.5-5 9-5 9S1 8.5 1 5a5 5 0 0 1 5-5zm0 3a2 2 0 1 0 0 4 2 2 0 0 0 0-4z" fill="var(--teal)"/></svg>
        <span>4180 Lantern Ridge Rd, suite 210<br>Harbor Falls, Texas 78990</span>
      </div>
    </div>
    <div class="social" aria-label="Social channels">
      <span class="social__item"></span>
      <span class="social__item"></span>
      <span class="social__item"></span>
      <span class="social__item"></span>
    </div>
  </section>
</main>
</body>
</html>
```